Building Defect timeline illustration

We need an memorable illustration using iconography to plot the time frame for a building defects process. These are typically shown in single line format and not catchy. Designed to stand out. Powerpoint of the timeline attached. Colour blue to be dominant please.Can use building/construction imagery/icons.

Target Market(s)

Builders/Developers/General public

Industry/Entity Type

Property

Font styles to use
Sans Serif

Colors
0355a3
3176b5
ffffff

Requirements
Must have
• Visual appeal, ability to stick to the factual timeline.
Nice to have
• You could incorporate building/construction into the graphics- suggestion only.

```html
<!DOCTYPE html>
<html lang="en">
<head>
<meta charset="utf-8">
<title>Project Timeline</title>
<link rel="stylesheet" href="https://fonts.googleapis.com/css2?family=Archivo+Black&family=Roboto:ital,wght@0,700;0,900;1,700;1,900&display=swap">
<style>
  :root {
    --blue-dark: #0b55a5;
    --blue-mid: #3176b5;
    --blue-light: #86bfe6;
    --mint: #d8ebec;
    --band: #afc3de;
    --ghost: #a9b9d8;
    --white: #ffffff;
  }
  html, body { margin: 0; padding: 0; overflow: hidden; }
  body { width: 1200px; height: 848px; background: var(--mint); }
  .poster {
    position: relative; width: 1200px; height: 848px; overflow: hidden;
    background: var(--mint);
    font-family: "Roboto", Arial, sans-serif;
    color: var(--blue-dark);
  }
  .artwork { position: absolute; inset: 0; }
  .label {
    position: absolute; margin: 0; text-align: center;
    font-style: italic; font-weight: 700; line-height: 1.2;
    transform: translateX(-50%);
  }
  .when { font-size: 17px; }
  .when--large { font-size: 19px; }
  .task { font-size: 19px; line-height: 1.27; }
  .task .emphasis { display: block; font-size: 28px; font-weight: 900; line-height: 1.1; }
  .badge-value {
    position: absolute; transform: translateX(-50%); text-align: center;
    font-style: italic; font-weight: 900; line-height: 1; margin: 0;
  }
  .badge-value .number { display: block; font-size: 36px; }
  .badge-value .unit { display: block; font-size: 19px; font-weight: 700; margin-top: 4px; }
  .badge-value--big .number { font-size: 40px; }
  .bond { position: absolute; left: 18px; top: 630px; font-style: italic; font-weight: 700; font-size: 18px; width: 190px; }
  .bond .bond-word { position: absolute; top: 0; }
  .tag { position: absolute; font-style: italic; font-weight: 900; font-size: 16px; margin: 0; }
  .figure-slot { position: absolute; border-radius: 6px; }
</style>
</head>
<body>
<main class="poster">
  <svg class="artwork" width="1200" height="848" viewBox="0 0 1200 848" aria-hidden="true">
    <defs>
      <g id="badge">
        <circle cx="7" cy="0" r="52" fill="var(--blue-dark)"/>
        <circle cx="0" cy="0" r="48" fill="var(--white)"/>
        <path d="M4 -57 A57 57 0 0 0 -38 42" fill="none" stroke="var(--blue-light)" stroke-width="6"/>
        <polygon points="-50,34 -28,50 -46,56" fill="var(--blue-light)"/>
      </g>
    </defs>

    <!-- header bands -->
    <rect x="0" y="0" width="1200" height="90" fill="var(--blue-light)"/>
    <polygon points="895,90 1200,36 1200,90" fill="var(--blue-dark)"/>

    <!-- footer band -->
    <polygon points="0,735 1200,800 1200,848 0,848" fill="var(--blue-light)"/>

    <!-- column shading -->
    <rect x="209" y="432" width="174" height="350" fill="var(--band)"/>
    <rect x="546" y="432" width="175" height="362" fill="var(--band)"/>
    <rect x="944" y="432" width="190" height="383" fill="var(--band)"/>

    <!-- title -->
    <text x="40" y="162" textLength="760" lengthAdjust="spacingAndGlyphs" font-family="Archivo Black, Arial Black, sans-serif" font-size="76" fill="var(--ghost)">PROJECT TIMELINE</text>
    <text x="36" y="108" textLength="840" lengthAdjust="spacingAndGlyphs" font-family="Archivo Black, Arial Black, sans-serif" font-size="84" fill="var(--blue-dark)" stroke="var(--white)" stroke-width="5" paint-order="stroke" stroke-linejoin="round">PROJECT TIMELINE</text>

    <!-- badges -->
    <use href="#badge" transform="translate(145 265)"/>
    <use href="#badge" transform="translate(290 272)"/>
    <use href="#badge" transform="translate(462 222) scale(1.12)"/>
    <use href="#badge" transform="translate(630 238) scale(1.08)"/>
    <use href="#badge" transform="translate(818 232) scale(1.08)"/>
    <use href="#badge" transform="translate(1044 165) scale(1.12)"/>

    <!-- clock hands -->
    <line x1="133" y1="272" x2="133" y2="228" stroke="var(--blue-dark)" stroke-width="6" stroke-linecap="round"/>
    <line x1="133" y1="272" x2="170" y2="252" stroke="var(--blue-dark)" stroke-width="6" stroke-linecap="round"/>
    <circle cx="133" cy="272" r="6" fill="var(--blue-dark)"/>

    <!-- timeline axis -->
    <line x1="48" y1="432" x2="1168" y2="432" stroke="var(--blue-dark)" stroke-width="6"/>
    <polygon points="30,432 62,418 54,432 62,446" fill="var(--blue-dark)"/>
    <polygon points="1186,432 1154,418 1162,432 1154,446" fill="var(--blue-dark)"/>

    <!-- milestone dots and leaders -->
    <g fill="var(--blue-light)" stroke="var(--blue-dark)" stroke-width="1.5">
      <circle cx="140" cy="432" r="28"/>
      <circle cx="288" cy="432" r="28"/>
      <circle cx="462" cy="432" r="28"/>
      <circle cx="632" cy="432" r="28"/>
      <circle cx="821" cy="432" r="28"/>
      <circle cx="1045" cy="432" r="28"/>
    </g>
    <g stroke="var(--blue-dark)" stroke-width="6" stroke-dasharray="4 3">
      <line x1="137" y1="462" x2="137" y2="600"/>
      <line x1="290" y1="462" x2="290" y2="512"/>
      <line x1="463" y1="462" x2="463" y2="512"/>
      <line x1="635" y1="462" x2="635" y2="512"/>
      <line x1="822" y1="462" x2="822" y2="512"/>
      <line x1="1045" y1="462" x2="1045" y2="512"/>
    </g>

    <!-- magnifier for bond -->
    <circle cx="128" cy="640" r="34" fill="var(--white)" stroke="var(--blue-dark)" stroke-width="8"/>
    <line x1="128" y1="676" x2="148" y2="716" stroke="var(--blue-dark)" stroke-width="13" stroke-linecap="round"/>
    <text x="128" y="650" text-anchor="middle" font-family="Roboto, Arial, sans-serif" font-weight="900" font-style="italic" font-size="28" fill="var(--blue-dark)">2%</text>

    <!-- interim clipboard -->
    <g transform="translate(428 612)">
      <rect x="0" y="12" width="86" height="118" rx="8" fill="var(--blue-dark)"/>
      <rect x="9" y="22" width="68" height="98" fill="var(--white)"/>
      <rect x="24" y="4" width="38" height="18" rx="4" fill="var(--blue-dark)"/>
      <g stroke="var(--blue-dark)" stroke-width="5" fill="none" stroke-linecap="round">
        <path d="M17 40 l5 5 l8 -9"/><line x1="38" y1="41" x2="68" y2="41"/>
        <path d="M17 60 l5 5 l8 -9"/><line x1="38" y1="61" x2="68" y2="61"/>
        <path d="M17 80 l5 5 l8 -9"/><line x1="38" y1="81" x2="68" y2="81"/>
        <path d="M17 100 l5 5 l8 -9"/><line x1="38" y1="101" x2="68" y2="101"/>
      </g>
    </g>

    <!-- final clipboard -->
    <g transform="translate(778 620)">
      <rect x="0" y="12" width="86" height="118" rx="8" fill="var(--blue-dark)"/>
      <rect x="9" y="22" width="68" height="98" fill="var(--white)"/>
      <rect x="24" y="4" width="38" height="18" rx="4" fill="var(--blue-dark)"/>
      <g stroke="var(--blue-dark)" stroke-width="5" fill="none" stroke-linecap="round">
        <path d="M17 40 l5 5 l8 -9"/><line x1="38" y1="41" x2="68" y2="41"/>
        <path d="M17 60 l5 5 l8 -9"/><line x1="38" y1="61" x2="68" y2="61"/>
        <path d="M17 80 l5 5 l8 -9"/><line x1="38" y1="81" x2="68" y2="81"/>
        <path d="M17 100 l5 5 l8 -9"/><line x1="38" y1="101" x2="68" y2="101"/>
      </g>
    </g>

    <!-- bell -->
    <g fill="none" stroke="var(--blue-dark)" stroke-width="9" stroke-linecap="round">
      <path d="M1000 705 Q1008 695 1008 668 Q1008 635 1035 630 Q1062 635 1062 668 Q1062 695 1070 705 Z" stroke-linejoin="round"/>
      <path d="M1022 713 Q1035 730 1048 713"/>
      <path d="M982 650 Q972 668 982 690"/>
      <path d="M968 640 Q952 668 968 702"/>
      <path d="M1088 650 Q1098 668 1088 690"/>
      <path d="M1102 640 Q1118 668 1102 702"/>
    </g>
    <circle cx="1035" cy="624" r="6" fill="var(--blue-dark)"/>
  </svg>

  <!-- badge values -->
  <p class="badge-value" style="left:290px; top:236px;"><span class="number">12</span><span class="unit">Months</span></p>
  <p class="badge-value" style="left:456px; top:206px;"><span class="number">15-18</span><span class="unit">Months</span></p>
  <p class="badge-value" style="left:630px; top:210px;"><span class="number">18</span><span class="unit">Months</span></p>
  <p class="badge-value" style="left:818px; top:210px;"><span class="number">21-24</span><span class="unit">Months</span></p>
  <p class="badge-value badge-value--big" style="left:1040px; top:150px;"><span class="number">24</span><span class="unit">Months</span></p>

  <!-- timing labels -->
  <p class="label when" style="left:140px; top:345px; width:150px;">Any time before OC issued</p>
  <p class="label when" style="left:290px; top:345px; width:160px;">Within 12 months of completion of building work</p>
  <p class="label when when--large" style="left:468px; top:308px; width:150px;">Within 15 – 18 months of completion of building work</p>
  <p class="label when when--large" style="left:637px; top:322px; width:180px;">Within 18 months of completion of building work</p>
  <p class="label when when--large" style="left:822px; top:322px; width:175px;">21 to 24 months after completion of building work</p>
  <p class="label when when--large" style="left:1072px; top:252px; width:210px;">2 years after completion of work within 60 days of date of final inspection report (whichever is the later)</p>

  <!-- task labels -->
  <p class="bond"><span class="bond-word" style="left:0;">Lodge</span><span class="bond-word" style="left:144px;">Bond</span></p>
  <p class="label task" style="left:290px; top:528px; width:170px;">Developer to appoint building inspector</p>
  <p class="label task" style="left:462px; top:528px; width:130px;">Interim report to be provided</p>
  <p class="label task" style="left:632px; top:526px; width:180px;">Developer to arrange building inspector to carry out <span class="emphasis">final</span>inspection</p>
  <p class="label task" style="left:822px; top:526px; width:130px;">Final report to be provided</p>
  <p class="label task" style="left:1032px; top:526px; width:140px;">Last date for claiming on bond</p>

  <p class="tag" style="left:386px; top:732px; transform:rotate(12deg);">INTERIM</p>
  <p class="tag" style="left:842px; top:738px; transform:rotate(-30deg);">FINAL</p>

  <!-- figure areas -->
  <div class="figure-slot" role="img" aria-label="Building inspector figure with hard hat and spanner" style="left:240px; top:604px; width:105px; height:115px; background:var(--blue-dark);"></div>
  <div class="figure-slot" role="img" aria-label="Building inspector figure holding a magnifying glass" style="left:560px; top:686px; width:140px; height:72px; background:var(--blue-dark);"></div>
</main>
</body>
</html>
```